PLUM BUSINESS CARD

Need a business card and logo. The company name is PLUM (Piedmont League of Ultimate Mareriders). It's a business that offers horseback riding lessons to young girls. Please put my name: Renata Bowley and a place for email and phone number. I would like the card to look feminine and soft. I like script type lettering. I want the card to be white or ivory with black or gray and hot pink print. A horse head outline would be cool, something whimsical. Think teen girl who likes glamour. Also, I give western riding lessons. So I like faded out background Images of western saddles, cowgirls, horses with long hair, ropes, horses in sunset...mabe the word PLUM can be made out of a lasso rope?

Just updated my project with a little more detail

Target Market(s)

Young girls/ cowgirls, western riding

Industry/Entity Type

Horseback Riding

Font styles to use
Script

Colors
e34197

Requirements
Must have
• A logo of PLUM.
Must say Piedmont League of Ultimate Mareriders
Colors are Pink and Black with an elegant, glamorous, feminine look.
Nice to have
• Could have a picture or outline of a horse

```html
<!DOCTYPE html>
<html lang="en">
<head>
<meta charset="utf-8">
<title>PLUM Business Card</title>
<link rel="stylesheet" href="https://fonts.googleapis.com/css2?family=Arimo:wght@400;700&display=swap">
<style>
  :root {
    --page-bg: #ffffff;
    --card-bg: #ffffff;
    --ink: #000000;
    --logo-pink: #d21ea6;
    --band-pink: #f80fd2;
    --swoosh-gray: #b3b3b3;
    --horse-gray: #d6d6d6;
  }
  html, body {
    margin: 0;
    padding: 0;
    width: 1200px;
    height: 1190px;
    overflow: hidden;
    background: var(--page-bg);
  }
  .canvas {
    position: relative;
    width: 1200px;
    height: 1190px;
  }
  .business-card {
    position: absolute;
    left: 411px;
    top: 277px;
    width: 300px;
    height: 522px;
    border: 1px solid var(--ink);
    background: var(--card-bg);
    overflow: hidden;
    font-family: "Arimo", Arial, sans-serif;
    color: var(--ink);
  }
  .brand-name {
    position: absolute;
    left: 0;
    top: 14px;
    width: 300px;
    margin: 0;
    text-align: center;
    font-family: "Arimo", Arial, sans-serif;
    font-weight: 700;
    font-size: 64px;
    line-height: 72px;
    letter-spacing: 10px;
    color: var(--logo-pink);
  }
  .brand-tagline {
    position: absolute;
    left: 20px;
    top: 99px;
    width: 282px;
    margin: 0;
    font-size: 12px;
    line-height: 14px;
    white-space: nowrap;
  }
  .horse-art {
    position: absolute;
    left: 38px;
    top: 148px;
    width: 233px;
    height: 221px;
    border-radius: 45% 55% 40% 50%;
    background: radial-gradient(ellipse at 50% 45%, var(--horse-gray) 0%, rgba(214,214,214,0.5) 55%, rgba(255,255,255,0) 75%);
  }
  .card-base {
    position: absolute;
    left: 0;
    top: 0;
  }
  .contact {
    position: absolute;
    left: 0;
    top: 420px;
    width: 300px;
    text-align: center;
    font-weight: 700;
  }
  .contact-name {
    margin: 0;
    font-size: 24px;
    line-height: 28px;
  }
  .contact-phone {
    margin: 8px 0 0;
    font-size: 19px;
    line-height: 22px;
  }
  .contact-email {
    margin: 2px 0 0;
    font-size: 16px;
    line-height: 20px;
  }
</style>
</head>
<body>
  <main class="canvas">
    <section class="business-card">
      <h1 class="brand-name">PLUM</h1>
      <p class="brand-tagline">Piedmont League of Ultimate Mareriders</p>

      <div class="horse-art" role="img" aria-label="Faint gray illustration of a horse head with a flowing mane"></div>

      <svg class="card-base" width="300" height="522" viewBox="0 0 300 522" aria-hidden="true">
        <path d="M0 398 Q150 382 300 338 L300 350 Q150 390 0 401 Z" fill="var(--swoosh-gray)"/>
        <path d="M0 401 Q150 390 300 350 L300 362 Q150 396 0 404 Z" fill="var(--ink)"/>
        <path d="M0 404 Q150 396 300 362 L300 522 L0 522 Z" fill="var(--band-pink)"/>
      </svg>

      <div class="contact">
        <p class="contact-name">Renata Bowley</p>
        <p class="contact-phone">(000) 000-0000</p>
        <p class="contact-email">email goes here</p>
      </div>
    </section>
  </main>
</body>
</html>
```